LMVBeacon online header

We need a header for our online internal company newsletter/blogsite. It is called the LMVBeacon which is a contraction between LMV (the department associated) and the word Gazette.
We want to have a new modern design for the header that should say "LMVBeacon" or "LMVBeacon online" (there used to be a paper version) in a nice artistic modern friendly inviting way. Sort of like a newspaper header.
There could be an optional text line that says "All the news you need" or something like that.
Target Market(s)
Consulting professionals in the area of mathematics, econometrics and IT
Industry/Entity Type
It Company
Logo Text
LMVBeacon
Colors
Designer to choose colors to be used in the design.
Look and feel

```html
<!DOCTYPE html>
<html lang="en">
<head>
<meta charset="utf-8">
<title>LMVBeacon — Online Header</title>
<link rel="stylesheet" href="https://fonts.googleapis.com/css2?family=Fira+Sans+Extra+Condensed:wght@700&display=swap">
<style>
  :root {
    --paper: #ffffff;
    --masthead-blue: #34628f;
    --band-deep: #3a74b0;
    --band-mid: #4a86c2;
    --band-light: #8fb9e0;
    --band-edge: #b9d4ee;
    --tagline: #ffffff;
    --hero-night: #0b1733;
    --hero-navy: #1b3563;
    --hero-glow: #bfe6f5;
    --hero-mist: #dde3ee;
    --hero-pale: #eef1f6;
  }
  * { margin: 0; padding: 0; box-sizing: border-box; }
  html, body {
    width: 927px;
    height: 1200px;
    overflow: hidden;
    background: var(--paper);
  }
  .page {
    position: relative;
    width: 927px;
    height: 1200px;
    background: var(--paper);
    font-family: "Fira Sans Extra Condensed", "Arial Narrow", sans-serif;
  }
  .hero-image {
    position: absolute;
    left: 0;
    top: 0;
    width: 927px;
    height: 452px;
    background:
      radial-gradient(ellipse 300px 190px at 220px 360px, rgba(235, 250, 255, 0.95) 0%, rgba(170, 225, 245, 0.85) 45%, transparent 80%),
      radial-gradient(ellipse 100px 95px at 260px 80px, rgba(150, 215, 240, 0.9), transparent 80%),
      radial-gradient(ellipse 80px 70px at 620px 70px, rgba(80, 165, 220, 0.85), transparent 80%),
      radial-gradient(ellipse 420px 300px at 120px 120px, var(--hero-night) 0%, var(--hero-navy) 55%, transparent 100%),
      linear-gradient(180deg, #9fb1cf 0%, var(--hero-mist) 45%, var(--hero-pale) 100%);
  }
  .masthead-title {
    position: absolute;
    right: 46px;
    top: 296px;
    font-size: 132px;
    font-weight: 700;
    line-height: 1;
    letter-spacing: -3px;
    color: var(--masthead-blue);
  }
  .tagline-band {
    position: absolute;
    left: 0;
    top: 444px;
    width: 927px;
    height: 58px;
    background: linear-gradient(180deg,
      var(--band-edge) 0px, var(--band-light) 6px,
      var(--band-mid) 10px, var(--band-deep) 44px,
      var(--band-light) 50px, var(--band-edge) 58px);
  }
  .tagline {
    position: absolute;
    right: 16px;
    top: 451px;
    font-size: 40px;
    font-weight: 700;
    line-height: 1;
    letter-spacing: -0.5px;
    color: var(--tagline);
  }
</style>
</head>
<body>
  <main class="page">
    <div class="hero-image" role="img" aria-label="Photograph of a close-up eye reflecting the globe, with glowing blue globes floating on a dark background"></div>
    <div class="tagline-band"></div>
    <h1 class="masthead-title">LMVBeacon</h1>
    <p class="tagline">The news you need, when you need it.</p>
  </main>
</body>
</html>
```